Stationery Design Project

Minimal Design. Black and White Colours Only.
Need Business Card
With Compliments slip
Letterhead
A4 Folder

Target Market(s)

Luxury architectual designed home owners

Industry/Entity Type

Business

Requirements
Must have
• Black and White colours only. Suggest some good textured stock for business card for future printing. try to use font that is used in my logo our some other minimal modern font.

```html
<!DOCTYPE html>
<html lang="en">
<head>
<meta charset="utf-8">
<title>Calder Estates – Business Card</title>
<link rel="stylesheet" href="https://fonts.googleapis.com/css2?family=Montserrat:wght@600&family=Pinyon+Script&family=Courgette&display=swap">
<style>
  :root {
    --paper: #ffffff;
    --card-dark: #0d0d0d;
    --card-mid: #2a2a2a;
    --ink-light: #ffffff;
    --ink-silver: #c4c4c4;
  }
  html, body {
    margin: 0;
    padding: 0;
    width: 1200px;
    height: 359px;
    overflow: hidden;
    background: var(--paper);
  }
  .sheet {
    position: relative;
    width: 1200px;
    height: 359px;
  }
  .card {
    position: absolute;
    top: 0;
    height: 359px;
    overflow: hidden;
    background: linear-gradient(160deg, var(--card-mid) 0%, var(--card-dark) 45%, #1c1c1c 70%, var(--card-dark) 100%);
    color: var(--ink-light);
  }
  .card--front { left: 0; width: 587px; }
  .card--back { left: 613px; width: 587px; }

  .brand {
    position: absolute;
    display: flex;
    align-items: center;
    gap: 12px;
    font-family: "Montserrat", sans-serif;
    font-weight: 600;
    white-space: nowrap;
  }
  .brand__mark {
    display: block;
    background: currentColor;
  }
  .card--front .brand {
    left: 36px;
    top: 34px;
    font-size: 18px;
    color: var(--ink-light);
  }
  .card--front .brand__mark { width: 26px; height: 26px; }
  .card--back .brand {
    left: 106px;
    top: 160px;
    font-size: 26px;
    color: var(--ink-silver);
  }
  .card--back .brand__mark { width: 40px; height: 40px; }

  .holder {
    position: absolute;
    left: 24px;
    top: 118px;
    width: 228px;
    text-align: center;
  }
  .holder__name {
    margin: 0;
    font-family: "Pinyon Script", cursive;
    font-weight: 400;
    font-size: 40px;
    line-height: 46px;
    border-bottom: 1.5px solid var(--ink-light);
  }
  .holder__role {
    margin: 2px 0 0;
    font-family: "Pinyon Script", cursive;
    font-size: 19px;
  }

  .contact {
    position: absolute;
    margin: 0;
    padding: 0;
    list-style: none;
    font-family: "Courgette", cursive;
    font-size: 16px;
    line-height: 22px;
  }
  .contact li {
    display: flex;
    align-items: center;
    gap: 8px;
    margin-bottom: 14px;
  }
  .contact svg { flex: none; fill: var(--ink-light); }
  .contact--phones { left: 30px; top: 265px; }
  .contact--phones li { margin-bottom: 16px; }
  .contact--details { left: 285px; top: 206px; font-size: 15px; }
  .contact--details li { margin-bottom: 12px; }
</style>
</head>
<body>
<main class="sheet">
  <section class="card card--front" aria-label="Business card front">
    <div class="brand"><span class="brand__mark"></span>CALDER ESTATES</div>

    <div class="holder">
      <h1 class="holder__name">Marcus Hale</h1>
      <p class="holder__role">Managing Director</p>
    </div>

    <ul class="contact contact--phones">
      <li>
        <svg width="24" height="30" viewBox="0 0 24 30" aria-hidden="true"><path d="M3 1h18a2 2 0 0 1 2 2v24a2 2 0 0 1-2 2H3a2 2 0 0 1-2-2V3a2 2 0 0 1 2-2zm1 4v19h16V5z"/></svg>
        +61 412 555 018
      </li>
      <li>
        <svg width="24" height="20" viewBox="0 0 24 20" aria-hidden="true"><path d="M2 3c6-3 14-3 20 0v4h-5V5c-3-1-7-1-10 0v2H2zM5 9h14l3 9H2zm7 2a3 3 0 1 0 0 6 3 3 0 0 0 0-6z"/></svg>
        +61 7 3555 0142
      </li>
    </ul>

    <ul class="contact contact--details">
      <li>
        <svg width="30" height="26" viewBox="0 0 30 26" aria-hidden="true"><path d="M15 1 1 13h4v12h7v-8h6v8h7V13h4z"/></svg>
        <span>Level 21, 48 Harbour Rd<br>Brisbane QLD 4000 Australia</span>
      </li>
      <li>
        <svg width="30" height="30" viewBox="0 0 30 30" aria-hidden="true"><path d="M15 1a14 14 0 1 0 0 28 14 14 0 0 0 0-28zm0 2.5a11.5 11.5 0 0 1 11 8H4a11.5 11.5 0 0 1 11-8zM4 18.5h22a11.5 11.5 0 0 1-22 0z"/></svg>
        calderestates.com
      </li>
      <li>
        <svg width="30" height="30" viewBox="0 0 30 30" aria-hidden="true"><path d="M2 12 15 2l13 10v16H2zm3 2 10 8 10-8v11H5z"/></svg>
        mhale@calderestates.com
      </li>
    </ul>
  </section>

  <section class="card card--back" aria-label="Business card back">
    <div class="brand"><span class="brand__mark"></span>CALDER ESTATES</div>
  </section>
</main>
</body>
</html>
```